Agriculture Business Need a Responsive Web Design

We need a Responsive Web Design for a Agriculture Business
We deliver agriculture data insight for farmers, media, salespersons and other that have an interrest in Agriculture.
Our products is a Velmorix - a application that helps people with insight on farms, and what this farms have deliveried of products. Products like Milk, grains, eggs, slaughtering of livestock, chicken, sheep and other slaughter of animals. Data about size of farms. We deliver stats about these farms. Compeare farms.

Target Market(s)

Agriculture businesses

Industry/Entity Type

Agriculture

Number of Pages Required

1 page

Font styles to use
Sans Serif

Requirements
Must have
• Responsive design. I.e the design shall be used on smartphones to desktop browsers. I think 2 columns on big screens that will collapse to 1 one small screens.

```html
<!DOCTYPE html>
<html lang="en">
<head>
<meta charset="utf-8">
<title>Velmorix — Insight on demand</title>
<link href="https://fonts.googleapis.com/css2?family=Source+Sans+3:ital,wght@0,300;0,400;0,600;0,700;1,300;1,400;1,600;1,700&display=swap" rel="stylesheet">
<style>
:root{
  --page:#f8f8f8;
  --ink:#333;
  --brand:#7dc242;
  --blue:#1a8fd6;
  --red:#e84c3d;
  --green:#2ecc71;
  --navy:#2980b9;
  --dark:#3f3f3f;
  --darker:#2c2c2c;
  --white:#fff;
}
*{box-sizing:border-box;margin:0;padding:0}
html,body{width:843px;height:1200px;overflow:hidden}
body{background:var(--page);font-family:"Source Sans 3",sans-serif;color:var(--ink);position:relative}
.abs{position:absolute}

.main-nav a{position:absolute;top:6px;font-size:8px;font-weight:600;color:#222;text-decoration:none}
.main-nav .active{color:var(--brand)}
.main-nav .underline{position:absolute;left:493px;top:18px;width:44px;height:2px;background:var(--brand)}

.brand-name{left:56px;top:34px;font-size:60px;font-weight:700;color:var(--brand);letter-spacing:-1px;line-height:1}
.btn-data,.btn-signup{top:56px;width:133px;height:33px;font-size:11px;font-weight:700;letter-spacing:.8px;display:flex;align-items:center;justify-content:center}
.btn-data{left:489px;background:var(--blue);color:var(--white)}
.btn-signup{left:652px;background:#e6e6e6;border:1px solid #cfcfcf;color:#333}

.hero{left:0;top:107px;width:843px;height:308px;overflow:hidden;
  background:linear-gradient(180deg,#b9c7cf 0%,#8fa39a 14%,#5f7d45 24%,#6fa83c 40%,#4f9a2a 70%,#63b036 100%)}
.hero-title{left:58px;top:140px;width:292px;height:45px;background:rgba(90,100,110,.7);color:var(--white);
  font-size:36px;font-weight:300;font-style:italic;display:flex;align-items:center;padding-left:7px;white-space:nowrap}
.hero-text{left:100px;top:194px;width:213px;height:54px;background:rgba(70,100,40,.7);color:var(--white);
  font-size:7.3px;font-style:italic;line-height:1.4;text-align:center;padding:3px 8px}
.hero-btn{left:163px;top:262px;width:88px;height:19px;background:#2b2b2b;color:var(--white);font-size:7px;font-weight:700;display:flex;align-items:center;justify-content:center;border-radius:2px}

.dashboard-back{left:356px;top:225px;width:70px;height:190px;background:linear-gradient(180deg,#e9e9e9 0%,#e9e9e9 18%,#fafafa 18%,#f4f4f4 100%)}
.dashboard-main{left:418px;top:175px;width:371px;height:240px;border-radius:3px 3px 0 0;
  background:linear-gradient(180deg,#4a4a4a 0%,#4a4a4a 9%,#ececec 9%,#ececec 17%,#ffffff 17%,#f6f6f6 100%)}

.card{top:469px;width:223px;height:325px;background:var(--white);box-shadow:0 2px 8px rgba(0,0,0,.18)}
.card-head{height:33px;color:var(--white);font-size:14.5px;font-weight:700;font-style:italic;display:flex;align-items:center;justify-content:center}
.card-media{height:184px;position:relative}
.card-text{font-size:9.2px;font-style:italic;color:#444;line-height:1.3;text-align:center;padding:10px 19px 0}
.card-btn{position:absolute;left:63px;top:286px;width:97px;height:24px;color:var(--white);font-size:8px;font-weight:700;display:flex;align-items:center;justify-content:center;border-radius:2px}
.red{background:var(--red)} .green{background:var(--green)} .navy{background:var(--navy)}

.news-title{left:0;width:843px;top:830px;text-align:center;font-size:23px;font-weight:300;font-style:italic;color:#444}
.news-text{left:270px;width:303px;top:874px;text-align:center;font-size:7.8px;font-style:italic;color:#555;line-height:1.35}
.news-input{left:278px;top:925px;width:207px;height:33px;border:1px solid #999;background:var(--white);font-size:8px;font-style:italic;color:#999;padding:12px 0 0 19px}
.news-btn{left:484px;top:925px;width:82px;height:33px;background:var(--darker);color:var(--white);font-size:8.5px;font-weight:700;display:flex;align-items:center;justify-content:center}

.footer{left:0;top:987px;width:843px;height:213px;background:var(--dark);color:var(--white)}
.contact{position:absolute;width:180px;text-align:center;font-size:10.5px;font-style:italic;line-height:1.3}
.contact svg{display:block;margin:0 auto 8px}
.foot-col{position:absolute;top:128px;font-size:6.8px;line-height:12.5px}
.foot-col h4{font-size:8px;font-weight:700;margin-bottom:2px}
.social{position:absolute;top:145px;width:21px;height:21px}
</style>
</head>
<body>

<nav class="main-nav">
  <a class="active" style="left:506px">Home</a>
  <a style="left:567px">Product</a>
  <a style="left:629px">FAQs</a>
  <a style="left:691px">About Us</a>
  <a style="left:752px">Contact Us</a>
  <span class="underline"></span>
</nav>

<div class="abs brand-name">Velmorix</div>
<div class="abs btn-data">GET THE DATA</div>
<div class="abs btn-signup">SIGN UP</div>

<section class="abs hero" role="img" aria-label="Soft-focus photograph of a green farm field under a pale sky"></section>
<h1 class="abs hero-title">Insight&nbsp; on demand</h1>
<p class="abs hero-text">Lorem ipsum dolor sit amet, consectetuer adipiscing elit. Phasellus hendrerit. Pellentesque aliquet nibh nec urna. In nisi neque, aliquet vel, dapibus id, mattis vel, nisi. Sed pretium, ligula sollicitudin laoreet viverra, tortor libero</p>
<div class="abs hero-btn">More Information</div>

<div class="abs dashboard-back" role="img" aria-label="Illustration of a second browser window showing dashboard charts"></div>
<div class="abs dashboard-main" role="img" aria-label="Illustration of a browser window showing a dashboard of charts and gauges"></div>

<article class="abs card" style="left:62px">
  <div class="card-head red">Analysis and Insight</div>
  <div class="card-media">
    <svg width="223" height="184" viewBox="0 0 223 184">
      <g stroke="#ddd" stroke-width="0.7">
        <line x1="36" y1="29" x2="198" y2="29"/><line x1="36" y1="60" x2="198" y2="60"/><line x1="36" y1="92" x2="198" y2="92"/><line x1="36" y1="124" x2="198" y2="124"/><line x1="36" y1="156" x2="198" y2="156"/>
      </g>
      <g font-family="Source Sans 3, sans-serif" font-size="9" fill="#444">
        <text x="21" y="32">40</text><text x="21" y="63">30</text><text x="21" y="95">20</text><text x="21" y="127">10</text><text x="24" y="159">0</text>
        <text x="32" y="178">2011</text><text x="81" y="178">2012</text><text x="130" y="178">2013</text><text x="178" y="178">2014</text>
      </g>
      <path d="M36 115 C50 104, 60 96, 82 94 C100 92, 115 72, 125 76 C145 82, 160 95, 184 136" fill="none" stroke="#e6178a" stroke-width="1.6"/>
      <path d="M36 145 C60 125, 85 120, 105 114 C120 110, 135 104, 146 94 C160 85, 170 75, 193 28" fill="none" stroke="#1a8fd6" stroke-width="1.6"/>
      <g fill="#e6178a"><circle cx="36" cy="115" r="3"/><circle cx="82" cy="94" r="3"/><circle cx="125" cy="76" r="3"/><circle cx="184" cy="136" r="3"/></g>
      <g fill="#1a8fd6"><circle cx="36" cy="145" r="3"/><circle cx="146" cy="94" r="3"/><circle cx="177" cy="63" r="3"/><circle cx="193" cy="28" r="3"/></g>
    </svg>
  </div>
  <p class="card-text">Lorem ipsum dolor sit amet, consectetuer adipi-scing elit. Phasellus hendrerit. Pellentesque aliquet nibh nec urna. In nisi neque, aliquet vel, dapibus id, mattis vel.</p>
  <div class="card-btn red">Read More</div>
</article>

<article class="abs card" style="left:309px">
  <div class="card-head green">Farms</div>
  <div class="card-media" role="img" aria-label="Photograph of cattle grazing in a green pasture at sunset" style="background:linear-gradient(180deg,#5d6f82 0%,#a7aeb0 35%,#d9c79a 48%,#3f5a25 58%,#5b7f2b 80%,#3d5a1c 100%)"></div>
  <p class="card-text">Lorem ipsum dolor sit amet, consectetuer adipi-scing elit. Phasellus hendrerit. Pellentesque aliquet nibh nec urna. In nisi neque, aliquet vel, dapibus id, mattis vel.</p>
  <div class="card-btn green">Read More</div>
</article>

<article class="abs card" style="left:557px">
  <div class="card-head navy">Produce</div>
  <div class="card-media" role="img" aria-label="Photograph of a combine harvester unloading grain into a trailer" style="background:linear-gradient(160deg,#6f9fd0 0%,#b9cbdc 30%,#7f8f4a 50%,#6d7440 62%,#b99566 80%,#a98656 100%)"></div>
  <p class="card-text">Lorem ipsum dolor sit amet, consectetuer adipi-scing elit. Phasellus hendrerit. Pellentesque aliquet nibh nec urna. In nisi neque, aliquet vel, dapibus id, mattis vel.</p>
  <div class="card-btn navy">Read More</div>
</article>

<h2 class="abs news-title">Sign up for our free newsletter</h2>
<p class="abs news-text">Praesent dapibus, neque id cursus faucibus, tortor neque egestas augue, eu vulputate magna eros eu erat. Aliquam erat volutpat. Nam dui mi, tincidunt quis, accumsan porttitor, facilisis luctus, metus.</p>
<div class="abs news-input">Email Address</div>
<div class="abs news-btn">Sign Up</div>

<footer class="abs footer">
  <div class="contact" style="left:146px;top:16px">
    <svg width="28" height="30" viewBox="0 0 28 30"><path d="M2 12 L14 3 L26 12 V28 H2 Z" fill="#e84c3d"/><rect x="6" y="7" width="16" height="12" fill="#f4f4f4"/><path d="M2 12 L14 21 L26 12" fill="none" stroke="#b83a2e" stroke-width="1.2"/></svg>
    info@velmorix.com
  </div>
  <div class="contact" style="left:332px;top:16px">
    <svg width="24" height="30" viewBox="0 0 24 30"><ellipse cx="12" cy="26" rx="9" ry="3" fill="#2a6f9e"/><path d="M12 26 C6 18 3 14 3 10 A9 9 0 0 1 21 10 C21 14 18 18 12 26 Z" fill="#3ca0e0"/><circle cx="12" cy="10" r="3.5" fill="#fff"/></svg>
    214 Orchard Lane,<br>Millbrook,<br>Ohio
  </div>
  <div class="contact" style="left:516px;top:16px">
    <svg width="30" height="30" viewBox="0 0 30 30"><rect x="3" y="5" width="8" height="23" rx="2" fill="#2fb5a5"/><rect x="11" y="3" width="17" height="25" rx="2" fill="#f2a33a"/><g fill="#fff"><rect x="14" y="7" width="11" height="5"/><rect x="14" y="15" width="3" height="3"/><rect x="19" y="15" width="3" height="3"/><rect x="14" y="20" width="3" height="3"/><rect x="19" y="20" width="3" height="3"/></g></svg>
    555-014-2290
  </div>

  <div class="foot-col" style="left:295px"><h4>Navigation</h4>Home<br>Product<br>Faqs<br>About Us</div>
  <div class="foot-col" style="left:388px"><h4>Special Category</h4>Item one<br>Item two<br>Item three<br>Item four</div>
  <div class="foot-col" style="left:475px"><h4>Links</h4></div>
  <span class="social" style="left:475px;background:#1da1f2" role="img" aria-label="Social link"></span>
  <span class="social" style="left:500px;background:#3b5998" role="img" aria-label="Social link"></span>
  <span class="social" style="left:525px;background:#25d366" role="img" aria-label="Social link"></span>
</footer>

</body>
</html>
```